Brivena HK 10000mg brochure

We need to design a brochure with both english and chinese text. Our product is from Collagen and it is used for joint pain or osteoarthitis patien...
Updates

I would like to extend this dateline for another 5 days. Not sure how to change this in PixelForge as it is not user friendly to me, but if you are reading this, please take note the new dateline is now 9th November . So please feel free to have sufficient time to submit in your awesome designs to us.!

Target Market(s)

40-70 years old

Industry/Entity Type

Pharmacy

Requirements
Must have
• Please see attach files uploaded
Nice to have
• Nice to have pictures showing ppl of all walks of life suffering joint problems from their work, leisure, exercise etc. Should have more clinical and proffesional looking charts
Should not have
• Too colourful.

```html
<!DOCTYPE html>
<html lang="zh">
<head>
<meta charset="utf-8">
<title>Brivena Collagen Hydrolysate</title>
<link href="https://fonts.googleapis.com/css2?family=Roboto:wght@300;400;500;700;900&family=Noto+Sans+SC:wght@300;400;700&display=swap" rel="stylesheet">
<style>
  :root {
    --sea-top: #38AFD0;
    --sea-mid: #45B6D5;
    --sea-bottom: #66C3DC;
    --salmon: #F4977C;
    --sand: #FBD97F;
    --white: #FFFFFF;
    --rule: rgba(255,255,255,0.55);
  }
  html, body { margin: 0; padding: 0; overflow: hidden; }
  body { width: 927px; height: 1200px; }
  .brochure {
    position: relative;
    width: 927px; height: 1200px;
    overflow: hidden;
    background: linear-gradient(165deg, var(--sea-top) 0%, var(--sea-mid) 55%, var(--sea-bottom) 100%);
    color: var(--white);
    font-family: "Roboto", "Noto Sans SC", sans-serif;
  }
  .product-tag {
    position: absolute; left: 0; top: 34px; width: 408px; height: 140px;
    background: var(--salmon);
    text-align: center;
  }
  .product-tag .line1 { margin-top: 20px; font-size: 24px; font-weight: 400; letter-spacing: 1.5px; }
  .product-tag .line2 { margin-top: 2px; font-size: 34px; font-weight: 700; letter-spacing: 6px; }
  .product-tag .line3 { margin-top: 8px; font-size: 16px; letter-spacing: 1px; }
  .divider-v {
    position: absolute; left: 409px; top: 34px; width: 4px; height: 372px; background: var(--white);
  }
  .headline {
    position: absolute; left: 444px; top: 24px;
    font-size: 40px; line-height: 67px; font-weight: 300; letter-spacing: 2px;
    margin: 0;
  }
  .headline strong { font-weight: 700; letter-spacing: 1.5px; }
  .question {
    position: absolute; left: 40px; top: 264px; margin: 0;
    font-family: "Noto Sans SC", sans-serif;
    font-size: 55px; line-height: 80px; font-weight: 300; letter-spacing: 3px;
  }
  .question strong { font-weight: 700; }
  .symptoms {
    position: absolute; left: 38px; top: 452px; margin: 0; padding: 0; list-style: none;
    font-family: "Noto Sans SC", sans-serif; font-size: 19px; font-weight: 300; letter-spacing: 1.5px;
  }
  .symptoms li { height: 45.6px; line-height: 36px; }
  .symptoms .lead { margin-bottom: 0; }
  .symptoms .item::before { content: "•"; margin-right: 2px; }
  .joint-chart {
    position: absolute; left: 387px; top: 442px; width: 540px; height: 324px;
    background: radial-gradient(ellipse at 50% 45%, #FCE29A 0%, var(--sand) 70%);
  }
  .pitch-title {
    position: absolute; left: 46px; top: 804px; margin: 0;
    font-family: "Noto Sans SC", "Roboto", sans-serif;
    font-size: 30px; font-weight: 700; letter-spacing: 1px;
  }
  .pitch-body {
    position: absolute; left: 45px; top: 862px; width: 850px; margin: 0;
    font-family: "Noto Sans SC", "Roboto", sans-serif;
    font-size: 21px; line-height: 44px; font-weight: 300; letter-spacing: 1.2px;
  }
  .divider-h {
    position: absolute; left: 40px; top: 1014px; width: 610px; height: 1px; background: var(--rule);
  }
  .contact {
    position: absolute; left: 44px; top: 1034px; margin: 0; padding: 0; list-style: none;
    font-family: "Roboto", "Noto Sans SC", sans-serif; font-size: 18px; letter-spacing: 1px;
  }
  .contact li { display: flex; align-items: flex-start; height: 36.5px; line-height: 36px; }
  .contact svg { width: 24px; height: 36px; margin-right: 14px; flex: none; }
  .contact .indent { padding-left: 38px; }
  .brand-name {
    position: absolute; left: 690px; top: 978px; width: 190px; text-align: center;
    font-size: 44px; font-weight: 900; letter-spacing: 2px;
  }
  .social { position: absolute; left: 658px; top: 1078px; display: flex; gap: 21px; }
  .social span {
    width: 36px; height: 36px; border: 2px solid var(--white); border-radius: 50%;
  }
</style>
</head>
<body>
<main class="brochure">
  <div class="product-tag">
    <div class="line1">BRIVENA COLLAGEN</div>
    <div class="line2">HYDROLYSATE</div>
    <div class="line3">10000MG POWDER</div>
  </div>
  <div class="divider-v"></div>
  <h1 class="headline">
    WE DISTRIBUTE<br>
    <strong>COLLGEN POWDER</strong><br>
    FOR JOINT HEALTH<br>
    OR THOSE SUFFER-<br>
    ING FROM<br>
    <strong>OSTEOARTHIRITIS</strong>
  </h1>

  <h2 class="question">你有关节<br><strong>疼痛吗？</strong></h2>

  <ul class="symptoms">
    <li class="lead">一些关节疼痛的最初迹象包括：</li>
    <li class="item">关节肿胀</li>
    <li class="item">关节僵硬</li>
    <li class="item">关节周围疼痛或紧张</li>
    <li class="item">站立时在膝盖处磨削声音</li>
    <li class="item">锻炼时难以移动关节</li>
    <li class="item">运动时关节疼痛</li>
  </ul>

  <div class="joint-chart" role="img" aria-label="Medical illustration comparing a normal joint, an osteoarthritic joint and a rheumatoid arthritic joint, titled Normal and Arthritic Joints"></div>

  <h3 class="pitch-title">与BRIVENA保持和缓解关节疼痛</h3>
  <p class="pitch-body">BRIVENA含有来自德国的100%纯胶原水解产物，有助于刺激关节软骨细胞的生长。它提供了一个安全和方便的方式来帮助补充身体的胶原蛋白供应</p>

  <div class="divider-h"></div>

  <ul class="contact">
    <li>
      <svg viewBox="0 0 24 36" aria-hidden="true"><path d="M6 10c1-1 2-1 3 0l2 3c.6 1 .3 1.6-.5 2.3l-1 .8c.8 2 2.4 3.6 4.4 4.4l.8-1c.7-.8 1.3-1.1 2.3-.5l3 2c1 1 1 2 0 3l-1.3 1.2C15 26.5 5 17 5.8 11.3z" fill="#fff"/></svg>
      <span>0123456789</span>
    </li>
    <li>
      <svg viewBox="0 0 24 36" aria-hidden="true"><rect x="2" y="11" width="20" height="14" fill="none" stroke="#fff" stroke-width="2"/><path d="M2 11l10 8 10-8M2 25l7-7M22 25l-7-7" fill="none" stroke="#fff" stroke-width="2"/></svg>
      <span>info@brivena-care.com</span>
    </li>
    <li>
      <svg viewBox="0 0 24 36" aria-hidden="true"><path d="M12 8a6 6 0 0 1 6 6c0 4.5-6 11-6 11s-6-6.5-6-11a6 6 0 0 1 6-6z" fill="#fff"/><circle cx="12" cy="14" r="2.2" fill="#45B6D5"/></svg>
      <span>1234 街道名称,</span>
    </li>
    <li class="indent">位置名称</li>
  </ul>

  <div class="brand-name">BRIVENA</div>
  <div class="social" aria-label="Social media links">
    <span></span><span></span><span></span><span></span>
  </div>
</main>
</body>
</html>
```